Flyer Design Project

I am looking to redesign a flyer and get a few new ideas and looks.

The tag line should be changed to The Original Buzz Killers instead of the Safe Way to Spray.

We are a residential mosquito spraying company.
Updates

Thank oyu for submissions, I like the looks so far, Please do not be afraid to think outside the box with some off the cuff creative designs with different types of photos and graphics.  We are open to all suggestions.  Payment will be made for this project.  

Industry/Entity Type

Residential

Requirements
Must have
• Must incorporate Fenwick Larchmonts logo, do not want logo with frog changed.

```html
<!DOCTYPE html>
<html lang="en">
<head>
<meta charset="utf-8">
<title>Fenwick Larchmonts – Flyer</title>
<link rel="stylesheet" href="https://fonts.googleapis.com/css2?family=Montserrat:wght@500&family=Cinzel:wght@900&family=Fondamento:ital@1&family=Courgette&display=swap">
<style>
  :root {
    --blue-deep: #0a2f8f;
    --blue-mid: #1550c8;
    --red: #e0101a;
    --ink: #0b0b0b;
    --white: #ffffff;
    --mark-green: #7fd62b;
    --sky-top: #8ccbf0;
    --sky-low: #f4f8fb;
    --hill: #5f9a58;
    --grass: #4fbf1f;
    --house: #dfe6ee;
    --people: #e9e4e4;
    --shirt: #8fd0e8;
  }
  html, body {
    margin: 0;
    padding: 0;
    width: 1000px;
    height: 1200px;
    overflow: hidden;
    background: var(--white);
  }
  .flyer {
    position: relative;
    width: 1000px;
    height: 1200px;
    overflow: hidden;
    background: var(--white);
  }
  .scene-photo {
    position: absolute;
    left: 0;
    top: 180px;
    width: 1000px;
    height: 940px;
    background:
      radial-gradient(ellipse 220px 200px at 200px 800px, rgba(233,228,228,0.95), rgba(233,228,228,0) 100%),
      radial-gradient(ellipse 160px 170px at 520px 780px, rgba(143,208,232,0.9), rgba(143,208,232,0) 100%),
      radial-gradient(ellipse 200px 130px at 360px 660px, rgba(60,45,40,0.55), rgba(60,45,40,0) 100%),
      radial-gradient(ellipse 260px 170px at 760px 530px, rgba(223,230,238,0.95), rgba(223,230,238,0) 100%),
      radial-gradient(ellipse 240px 60px at 650px 560px, rgba(120,100,80,0.55), rgba(120,100,80,0) 100%),
      linear-gradient(180deg,
        var(--sky-top) 0%,
        #c9e6f7 22%,
        var(--sky-low) 44%,
        #e8f0ee 50%,
        var(--hill) 58%,
        #6aa860 63%,
        var(--grass) 72%,
        #45a91a 100%);
  }
  .waves {
    position: absolute;
    inset: 0;
    width: 1000px;
    height: 1200px;
  }
  .brand {
    position: absolute;
    left: 44px;
    top: 40px;
    display: flex;
    align-items: center;
    gap: 24px;
  }
  .brand-dot {
    width: 120px;
    height: 120px;
    border-radius: 50%;
    background: var(--mark-green);
  }
  .brand-name {
    font-family: "Montserrat", sans-serif;
    font-weight: 500;
    font-size: 64px;
    line-height: 1;
    color: var(--white);
    text-transform: uppercase;
    letter-spacing: 1px;
  }
  .tagline {
    position: absolute;
    left: 40px;
    top: 186px;
    margin: 0;
    font-family: "Fondamento", cursive;
    font-style: italic;
    font-size: 50px;
    font-weight: 400;
    letter-spacing: 3px;
    color: var(--red);
    text-shadow: 0 0 3px var(--white), 0 0 3px var(--white), 1px 1px 0 var(--white);
  }
  .headline {
    position: absolute;
    left: 40px;
    width: 935px;
    top: 386px;
    margin: 0;
    text-align: center;
    font-family: "Cinzel", serif;
    font-weight: 900;
    font-size: 66px;
    line-height: 1;
    white-space: nowrap;
    color: var(--red);
    -webkit-text-stroke: 2px var(--white);
    text-shadow:
      0 0 4px var(--ink), 0 0 4px var(--ink), 0 0 8px var(--ink),
      3px 3px 0 var(--ink), -3px -3px 0 var(--ink), 3px -3px 0 var(--ink), -3px 3px 0 var(--ink);
  }
  .lede {
    position: absolute;
    left: 42px;
    top: 490px;
    width: 840px;
    margin: 0;
    font-family: "Courgette", cursive;
    font-size: 38px;
    line-height: 46px;
    letter-spacing: 0.5px;
    color: var(--red);
    text-shadow: 1px 1px 0 var(--white), -1px -1px 0 var(--white), 2px 2px 3px rgba(0,0,0,0.35);
  }
</style>
</head>
<body>
<main class="flyer">
  <div class="scene-photo" role="img" aria-label="Photo of a smiling family of four on a green lawn in front of a white house, a boy pointing at a large mosquito near the house, green hills under a blue sky"></div>

  <svg class="waves" viewBox="0 0 1000 1200" aria-hidden="true">
    <defs>
      <linearGradient id="topBand" x1="0" y1="0" x2="0" y2="1">
        <stop offset="0" stop-color="#0d3aa8"/>
        <stop offset="0.6" stop-color="#1a5ad6"/>
        <stop offset="1" stop-color="#0a2f8f"/>
      </linearGradient>
      <linearGradient id="bottomBand" x1="0" y1="0" x2="0" y2="1">
        <stop offset="0" stop-color="#1550c8"/>
        <stop offset="1" stop-color="#0a2f8f"/>
      </linearGradient>
    </defs>
    <path d="M0 0 H1000 V200 C820 190 650 230 480 280 C330 325 170 330 0 300 Z" fill="url(#topBand)"/>
    <path d="M0 300 C170 330 330 325 480 280 C650 230 820 190 1000 200" fill="none" stroke="#ffffff" stroke-width="4"/>
    <path d="M0 1200 V1105 C200 1075 380 1060 560 1040 C740 1020 880 1000 1000 1000 V1200 Z" fill="url(#bottomBand)"/>
    <path d="M0 1105 C200 1075 380 1060 560 1040 C740 1020 880 1000 1000 1000" fill="none" stroke="#ffffff" stroke-width="4"/>
  </svg>

  <div class="brand">
    <span class="brand-dot"></span>
    <span class="brand-name">Fenwick<br>Larchmonts</span>
  </div>

  <p class="tagline">The Original Buzz Killers</p>

  <h1 class="headline">NO MORE MOSQUITOES</h1>

  <p class="lede">Let Fenwick Larchmonts protect your<br>health and return joy to your outdoor living</p>
</main>
</body>
</html>
```